Coastal Gin Label Design

We are needing a nautical/coastal themed label for our upcoming gin release.

We have saltbush, cucumber, juniper, and quandong being used in this gin.

Name of the Gin; Harbor Nights

The logo attached is the company logo, but doesn't have to be used on the front of the label, ie it can just be the name Fernholdes somewhere on the front.
Bottle specs attached as well so you can accurately represent the bottle- this bottle is also clear.

Target Market(s)

Women 25- 45

Font styles to use
Serif
Decorative

Colors
d5edf4
86cae7
33a6d7
86cfc6
cfeae6
ffffff
f6faec
ecf7fb
fefeff

Requirements
Must have
• Ocean/Coastal vibe to the label
Nice to have
• Blues,Whites clean and crisp
Should not have
• No generic word art look to it.
A dark mood

```html
<!DOCTYPE html>
<html lang="en">
<head>
<meta charset="utf-8">
<title>Fernholdes Harbor Nights Gin Label</title>
<link rel="stylesheet" href="https://fonts.googleapis.com/css2?family=Cinzel:wght@500&family=Bungee&family=Montserrat:wght@600&family=Oswald:wght@300&display=swap">
<style>
  :root {
    --page: #ffffff;
    --label: #ffffff;
    --gold: #b8973f;
    --gold-soft: #dcc588;
    --white: #ffffff;
    --sand: #eadfc4;
    --foam: #f4f8f6;
    --sea-light: #46bfb0;
    --sea-deep: #0f9a8c;
  }
  html, body {
    margin: 0;
    width: 1200px;
    height: 1193px;
    overflow: hidden;
    background: var(--page);
  }
  .label {
    position: absolute;
    left: 371px;
    top: 225px;
    width: 481px;
    height: 791px;
    background: var(--label);
    box-shadow: 0 6px 22px rgba(0,0,0,0.14);
    overflow: hidden;
  }
  .label__sea {
    position: absolute;
    left: 0;
    top: 0;
    width: 481px;
    height: 791px;
  }
  .label__maker {
    position: absolute;
    top: 52px;
    left: 0;
    width: 100%;
    text-align: center;
    font-family: "Cinzel", serif;
    font-weight: 500;
    font-size: 44px;
    letter-spacing: 1px;
    color: var(--gold);
    margin: 0;
  }
  .label__name {
    position: absolute;
    top: 222px;
    left: 0;
    width: 100%;
    text-align: center;
    font-family: "Bungee", sans-serif;
    font-size: 84px;
    line-height: 104px;
    color: var(--gold-soft);
    margin: 0;
    font-weight: 400;
  }
  .label__name span { display: block; }
  .label__type {
    position: absolute;
    top: 456px;
    left: 0;
    width: 100%;
    text-align: center;
    font-family: "Montserrat", sans-serif;
    font-weight: 600;
    font-size: 64px;
    letter-spacing: 6px;
    color: var(--white);
    text-shadow: 0 3px 6px rgba(0,0,0,0.35);
    margin: 0;
  }
  .label__rule {
    position: absolute;
    top: 699px;
    left: 112px;
    width: 249px;
    height: 2px;
    background: var(--white);
  }
  .label__specs {
    position: absolute;
    top: 713px;
    left: 0;
    width: 100%;
    text-align: center;
    font-family: "Oswald", sans-serif;
    font-weight: 300;
    font-size: 25px;
    color: var(--white);
    margin: 0;
    word-spacing: 2px;
  }
  .label__specs .gap { display: inline-block; width: 26px; }
</style>
</head>
<body>
  <main class="label">
    <svg class="label__sea" viewBox="0 0 481 791" role="img" aria-label="Aerial photograph of turquoise ocean waves breaking on a sandy shore">
      <defs>
        <linearGradient id="shoreGradient" x1="0" y1="0.35" x2="0.75" y2="1">
          <stop offset="0" stop-color="var(--foam)" stop-opacity="0"/>
          <stop offset="0.18" stop-color="var(--sand)"/>
          <stop offset="0.38" stop-color="var(--foam)"/>
          <stop offset="0.55" stop-color="var(--sea-light)"/>
          <stop offset="1" stop-color="var(--sea-deep)"/>
        </linearGradient>
      </defs>
      <path d="M481 425 C420 440 360 470 300 500 C230 540 150 580 90 620 C50 650 20 660 0 665 L0 791 L481 791 Z" fill="url(#shoreGradient)"/>
    </svg>
    <p class="label__maker">FERNHOLDES</p>
    <h1 class="label__name"><span>HARBOR</span><span>NIGHTS</span></h1>
    <p class="label__type">GIN</p>
    <div class="label__rule"></div>
    <p class="label__specs">42% ALC/VOL<span class="gap"></span>750ML</p>
  </main>
</body>
</html>
```